7 3/4 x 5 1/4 Annual Banquet Invitation

Design an invitation for our Chamber's annual banquet. It will be a single sided invitation 5 1/4" wide by 7 3/4" height that we will print in-house. Our logo is attached. The theme is "Serving Together". I was thinking of an image with two hands coming together in a handshake, perhaps intertwining our logo colors. This is just a thought. I am open for any suggestions! Text for the invitation should be as follows: The Board of Directors and Staff cordially invites you to attend the 64th Yearly Gathering & Micro-Trade Fair - Monday, January 22, 2018. 5:30 p.m. Social, 6:00 p.m. Dinner. Cedarvale Chapel, 4819 Harlan P. Moss Rd S, Brookhaven. Please RSVP by January 18, 2018.

Target Market(s)

This invitation will be printed and mailed to our membership.

Industry/Entity Type

Business Management

Colors
33a6d7
faa54b
0355a3
00a990

Requirements
Must have
• Event info as indentified above.
Nice to have
• Our Logo

```html
<!DOCTYPE html>
<html lang="en">
<head>
<meta charset="utf-8">
<title>Invitation – 64th Yearly Gathering</title>
<link rel="stylesheet" href="https://fonts.googleapis.com/css2?family=Open+Sans:wght@400&family=Roboto+Slab:wght@300;400&family=Playfair+Display:wght@500&family=Roboto:wght@400;700&display=swap">
<style>
  :root {
    --backdrop: #8a5208;
    --card: #fffaf2;
    --ink: #1a1a1a;
    --accent-line: #f39a3a;
    --divider: #c8962e;
    --diamond: #f6c85a;
    --leaf-dark: #8e560c;
    --leaf-mid: #f2a324;
    --leaf-light: #fbe98e;
    --chamber-blue: #1424e6;
  }
  * { margin: 0; padding: 0; box-sizing: border-box; }
  html, body { width: 1200px; height: 1200px; overflow: hidden; }
  body { background: var(--backdrop); position: relative; font-family: "Roboto Slab", serif; font-weight: 300; color: var(--ink); }

  .card {
    position: absolute; left: 194px; top: 0; width: 813px; height: 1200px;
    background: var(--card);
  }
  .foliage {
    position: absolute; left: 0; top: 0; width: 100%; height: 330px;
    background: linear-gradient(90deg, var(--leaf-dark) 0%, var(--leaf-mid) 45%, var(--leaf-light) 75%, var(--leaf-mid) 100%);
    -webkit-mask-image: linear-gradient(180deg, rgba(0,0,0,.85) 0%, rgba(0,0,0,.45) 55%, transparent 100%);
    mask-image: linear-gradient(180deg, rgba(0,0,0,.85) 0%, rgba(0,0,0,.45) 55%, transparent 100%);
  }
  .centered { position: absolute; left: 0; width: 100%; text-align: center; }

  .invitation-label {
    top: 304px; font-family: "Open Sans", sans-serif; font-weight: 400;
    font-size: 38px; letter-spacing: 10px; line-height: 1; padding-left: 10px;
  }
  .invitation-rule { position: absolute; left: 272px; top: 350px; width: 274px; height: 2px; background: var(--accent-line); }

  .host-line { top: 370px; font-size: 22px; line-height: 34px; font-weight: 300; }

  .event-title {
    top: 510px; font-family: "Playfair Display", serif; font-weight: 500;
    font-size: 64px; line-height: 1; letter-spacing: -2px;
  }
  .event-subtitle { top: 598px; font-size: 22px; font-weight: 300; }

  .divider { position: absolute; left: 152px; top: 686px; }

  .details { position: absolute; top: 718px; font-size: 16px; line-height: 34px; text-align: center; font-weight: 300; }
  .details--when { left: 140px; width: 262px; }
  .details--where { left: 402px; width: 280px; }

  .chamber { top: 908px; }
  .chamber-mark { display: block; margin: 0 auto 14px; width: 100px; height: 100px; border-radius: 50%; background: var(--chamber-blue); }
  .chamber-name {
    font-family: "Roboto", sans-serif; font-weight: 700; font-size: 26px;
    line-height: 30px; color: var(--chamber-blue); text-transform: uppercase;
  }

  .rsvp { top: 1134px; font-family: "Roboto", sans-serif; font-weight: 400; font-size: 26px; letter-spacing: 3px; }
</style>
</head>
<body>
  <main class="card">
    <div class="foliage" role="img" aria-label="Autumn branches with golden and amber leaves sweeping across the top"></div>

    <h2 class="centered invitation-label">invitation</h2>
    <div class="invitation-rule"></div>

    <p class="centered host-line">The Board of Directors and<br>Staff cordially invites you to attend</p>

    <h1 class="centered event-title">The 64th Yearly</h1>
    <p class="centered event-subtitle">Gathering &amp; Micro-Trade Fair</p>

    <svg class="divider" width="510" height="24" viewBox="0 0 510 24" aria-hidden="true">
      <line x1="0" y1="12" x2="235" y2="12" stroke="var(--divider)" stroke-width="1.5"/>
      <circle cx="238" cy="12" r="3" fill="var(--diamond)"/>
      <rect x="246" y="4" width="16" height="16" fill="var(--diamond)" transform="rotate(45 254 12)"/>
      <circle cx="272" cy="12" r="3" fill="var(--diamond)"/>
      <line x1="276" y1="12" x2="510" y2="12" stroke="var(--divider)" stroke-width="1.5"/>
    </svg>

    <div class="details details--when">
      Monday - January 22, 2018.<br>
      5:30 p.m. Social<br>
      6:00 p.m. Dinner.
    </div>
    <div class="details details--where">
      Cedarvale Chapel,<br>
      4819 Harlan P. Moss Rd S,<br>
      Brookhaven.
    </div>

    <div class="centered chamber">
      <span class="chamber-mark"></span>
      <p class="chamber-name">Lakemoor Chamber<br>of Commerce &amp; Tourism</p>
    </div>

    <p class="centered rsvp">Please RSVP by January 18, 2018.</p>
  </main>
</body>
</html>
```